Detail Shop Business card design

i need a business card design for my new detailing company called 'Brenner's Detail Shop'. i want an all black and white design . simple, direct and to the point. i want the designer to choose a fitting font to match the logothe front should have logo, address, phone and email and the back side should have a slogan and text indicating that we offer services on anything including cars, trucks, motorcycles and RVs. slogan will read "we take pride in your ride"
maybe also very small on the back side the IG icon with Brenners_Detail_Shop

phone 482.615.7734
address 7384 E Harlow Ave
Spokane WA 99342
email: BrennersDetail@quorvail.com

Target Market(s)

all ages , auto enthusiasts

Industry/Entity Type

Automotive

Contact Information for Business Card

the front should have logo, address, phone and email and the back side should have a slogan and text indicating that we offer services on anything including cars, trucks, motorcycles and RVs. slogan will read "we take pride in your ride"

phone 482.615.7734
address 7384 E Harlow Ave
Spokane WA 99342

Colors
000000
ffffff

Requirements
Must have
• bold font and very simple design with good spacing
Nice to have
• anything creative from the designer indicating we service any types of vehicles
Should not have
• any colors ,

```html
<!DOCTYPE html>
<html lang="en">
<head>
<meta charset="utf-8">
<title>Brenner's Detail Shop – Business Card</title>
<link rel="stylesheet" href="https://fonts.googleapis.com/css2?family=Oswald:wght@500;600&family=Open+Sans:wght@300;400&display=swap">
<style>
  :root {
    --backdrop: #4a4946;
    --card: #0d0d0d;
    --ink: #f2f2f2;
    --ink-soft: #cfcfcf;
  }
  * { box-sizing: border-box; margin: 0; padding: 0; }
  html, body { width: 1200px; height: 824px; overflow: hidden; }
  body {
    background: var(--backdrop);
    display: flex;
    align-items: center;
    justify-content: center;
    gap: 32px;
  }
  .card {
    position: relative;
    width: 552px;
    height: 316px;
    background: var(--card);
    border-radius: 3px;
    color: var(--ink);
    box-shadow: 0 10px 28px rgba(0,0,0,.45);
  }
  .brand {
    display: flex;
    flex-direction: column;
    align-items: center;
    gap: 8px;
  }
  .brand__mark {
    width: 34px; height: 34px;
    border: 2px solid var(--ink);
    border-radius: 50%;
  }
  .brand__name {
    font-family: "Oswald", sans-serif;
    font-weight: 600;
    font-size: 26px;
    letter-spacing: 1.5px;
    text-transform: uppercase;
    color: var(--ink);
  }
  /* Slogan side */
  .card--slogan {
    display: flex;
    flex-direction: column;
    align-items: center;
    justify-content: center;
    gap: 16px;
  }
  .slogan {
    font-family: "Oswald", sans-serif;
    font-weight: 600;
    font-size: 19px;
    letter-spacing: .5px;
    text-transform: uppercase;
  }
  .services {
    font-family: "Oswald", sans-serif;
    font-weight: 500;
    font-size: 17px;
    letter-spacing: 1.5px;
    text-transform: uppercase;
    color: var(--ink-soft);
  }
  /* Contact side */
  .card--contact .brand {
    position: absolute;
    top: 58px; left: 0; right: 0;
  }
  .contact {
    position: absolute;
    font-family: "Open Sans", sans-serif;
    font-weight: 300;
    font-size: 14px;
    color: var(--ink-soft);
    display: flex;
    align-items: center;
    gap: 8px;
  }
  .contact svg { width: 13px; height: 13px; fill: var(--ink-soft); flex: none; }
  .contact--phone   { left: 28px;  top: 198px; }
  .contact--address { left: 190px; top: 198px; }
  .contact--email   { left: 190px; top: 226px; }
  .contact--social  { left: 330px; top: 262px; }
  .social-square {
    width: 12px; height: 12px;
    border: 1.5px solid var(--ink-soft);
    border-radius: 2px;
    flex: none;
  }
</style>
</head>
<body>
  <section class="card card--slogan">
    <div class="brand">
      <span class="brand__mark"></span>
      <span class="brand__name">Brenner's Detail Shop</span>
    </div>
    <p class="slogan">We take pride in your ride</p>
    <p class="services">Cars | Trucks | Motorcycles | RVs</p>
  </section>

  <section class="card card--contact">
    <div class="brand">
      <span class="brand__mark"></span>
      <span class="brand__name">Brenner's Detail Shop</span>
    </div>

    <p class="contact contact--phone">
      <svg viewBox="0 0 16 16" aria-hidden="true"><path d="M3 1h3l1.5 4-2 1.3a9 9 0 0 0 4.2 4.2L11 8.5l4 1.5v3a2 2 0 0 1-2 2C6.4 15 1 9.6 1 3a2 2 0 0 1 2-2z"/></svg>
      482.615.7734
    </p>
    <p class="contact contact--address">
      <svg viewBox="0 0 16 16" aria-hidden="true"><path d="M8 0a5.5 5.5 0 0 0-5.5 5.5C2.5 10 8 16 8 16s5.5-6 5.5-10.5A5.5 5.5 0 0 0 8 0zm0 7.7a2.2 2.2 0 1 1 0-4.4 2.2 2.2 0 0 1 0 4.4z"/></svg>
      7384 E Harlow Ave, Spokane WA 99342
    </p>
    <p class="contact contact--email">
      <svg viewBox="0 0 16 16" aria-hidden="true"><path d="M1 3h14v10H1zm1.4 1.2L8 8.6l5.6-4.4z"/></svg>
      BrennersDetail@quorvail.com
    </p>
    <p class="contact contact--social">
      <span class="social-square"></span>
      Brenners_Detail_Shop
    </p>
  </section>
</body>
</html>
```